Attention grabbing 6x9 postcard

We are looking to have an attention grabbing post card that be sent out to homeowners from our roofing company Vell Roofing. the concept is that on the front it will say something like (STOP THE KNOCKING!
Tired of roofers knocking on your door? Contact us because we value your time as much as you value the roof over your head."
Vell Roofing
VellRoofing.example
555.672.VELL
info@vellroofing.example

Please feel free to come up with something very creative. Once we pick the final design we will provide the copy.

```html
<!DOCTYPE html>
<html lang="en">
<head>
<meta charset="utf-8">
<title>Vell Roofing Postcard</title>
<link href="https://fonts.googleapis.com/css2?family=Poppins:wght@400;500;600;700;800&display=swap" rel="stylesheet">
<style>
:root{
  --bg:#dcdcdc;
  --ink:#111111;
  --gold:#f2b51c;
  --white:#ffffff;
  --muted:#d9d9d9;
  --rule:#4a4a4a;
  --photo-dark:#5d5f5a;
  --photo-mid:#8a8b84;
  --photo-light:#b9b8b1;
  --stamp:#e6e6e6;
}
*{margin:0;padding:0;box-sizing:border-box}
html,body{width:1190px;height:1200px;overflow:hidden}
body{background:var(--bg);font-family:"Poppins",sans-serif;position:relative}
.card{position:absolute;left:235px;width:720px;height:480px;overflow:hidden}
.card-front{top:100px;background:linear-gradient(135deg,#1c1c1c,#0c0c0c)}
.card-back{top:620px;background:var(--white)}
.abs{position:absolute}
.art{position:absolute;left:0;top:0}
.headline{left:46px;top:40px;color:var(--white);font-weight:800;font-size:41px;line-height:43px;letter-spacing:-.5px}
.headline .accent{color:var(--gold);display:block}
.question{left:46px;top:168px;border-left:4px solid var(--gold);padding-left:16px;color:var(--white);font-weight:600;font-size:25px;line-height:29px}
.contact-title{font-weight:700;color:var(--gold);text-transform:uppercase}
.contact-title span{color:var(--white)}
.front-contact{left:46px;top:286px}
.front-contact .contact-title{font-size:18px;line-height:22px}
.front-contact p{color:var(--muted);font-size:12.5px;line-height:17px;margin-top:2px}
.divider{height:1px;background:var(--rule)}
.front-divider{left:46px;top:362px;width:380px}
.phone-line{display:flex;align-items:center;gap:8px;color:var(--white);font-weight:700}
.front-phone{left:46px;top:380px;font-size:29px}
.phone-line svg{flex:none}
.web{color:var(--white);font-weight:600;letter-spacing:.5px;white-space:nowrap}
.web b{color:var(--gold);font-weight:600}
.email-pill{display:inline-flex;align-items:center;gap:4px;border:1.5px solid var(--gold);border-radius:20px;color:var(--white);font-weight:500;white-space:nowrap}
.front-web{left:46px;top:425px;font-size:15px}
.front-email{left:258px;top:426px;font-size:9.5px;padding:2px 8px}
.brand-name{color:var(--ink);font-weight:700;white-space:nowrap}
.front-brand{left:596px;top:398px;font-size:18px}
.back-panel{left:0;top:0;width:359px;height:480px;background:linear-gradient(160deg,#1c1c1c,#0b0b0b)}
.process-title{left:40px;top:38px;color:var(--white);font-weight:800;font-size:27px;line-height:28px}
.process-title .accent{color:var(--gold);display:block}
.step{left:84px;width:196px;color:var(--white);font-size:9px;line-height:12px}
.back-contact{left:40px;top:280px}
.back-contact .contact-title{font-size:19px;line-height:22px;border-left:3px solid var(--gold);padding-left:7px;margin-left:-10px}
.back-contact p{color:var(--white);font-weight:600;font-size:12.5px;line-height:16px;margin-top:2px;width:200px}
.back-divider{left:40px;top:376px;width:300px}
.back-phone{left:40px;top:392px;font-size:17px}
.back-email{left:187px;top:393px;font-size:9.5px;padding:1px 8px}
.back-web{left:40px;top:424px;font-size:20px}
.back-brand{left:410px;top:66px;font-size:18px}
.stamp{left:615px;top:42px;width:62px;height:77px;background:var(--stamp)}
.address-line{left:460px;width:216px;height:1px;background:#c8c8c8}
</style>
</head>
<body>

<section class="card card-front">
  <svg class="art" width="720" height="480" viewBox="0 0 720 480">
    <polygon points="490,0 720,0 720,480 440,480" fill="var(--gold)"/>
    <g stroke="var(--white)" stroke-width="9" stroke-linejoin="round">
      <polygon role="img" aria-label="Photo: roofer cutting metal roof panels" points="434,232 403,286 341,286 310,232 341,178 403,178" fill="var(--photo-light)"/>
      <polygon role="img" aria-label="Photo: worker fastening roof sheeting" points="716,254 685,308 623,308 592,254 623,200 685,200" fill="var(--photo-mid)"/>
      <polygon role="img" aria-label="Photo: roofer in hard hat working on a roof" points="572,410 541,464 479,464 448,410 479,356 541,356" fill="#8f8a74"/>
      <polygon role="img" aria-label="Photo: roofer installing a dark metal roof on a countryside house" points="633,163 566,279 432,279 365,163 432,47 566,47" fill="var(--photo-dark)"/>
    </g>
  </svg>

  <h1 class="abs headline">STOP THE <span class="accent">KNOCKING!</span></h1>
  <p class="abs question">Tired of roofers<br>knocking on<br>your door?</p>

  <div class="abs front-contact">
    <h2 class="contact-title">Contact <span>Us</span></h2>
    <p>Because we value your time as much<br>as you value the roof over your head.</p>
  </div>

  <div class="abs divider front-divider"></div>

  <div class="abs phone-line front-phone">
    <svg width="22" height="22" viewBox="0 0 24 24"><circle cx="12" cy="12" r="12" fill="var(--gold)"/><path d="M8.2 6.5l2 2.2-1.1 1.6c.8 1.7 2 2.9 3.7 3.7l1.6-1.1 2.2 2-1.2 1.9c-4.6-.5-8.1-4-8.6-8.6z" fill="var(--ink)"/></svg>
    555.672.VELL
  </div>
  <div class="abs web front-web">www.<b>vellroofing</b>.example</div>
  <div class="abs email-pill front-email">
    <svg width="10" height="8" viewBox="0 0 10 8"><rect x=".5" y=".5" width="9" height="7" fill="none" stroke="var(--gold)"/><path d="M.5 .5L5 4.5 9.5 .5" fill="none" stroke="var(--gold)"/></svg>
    info@vellroofing.example
  </div>

  <div class="abs brand-name front-brand">Vell Roofing</div>
</section>

<section class="card card-back">
  <div class="abs back-panel"></div>

  <svg class="art" width="720" height="480" viewBox="0 0 720 480">
    <g fill="var(--gold)">
      <polygon points="72,127 64,141 48,141 40,127 48,113 64,113"/>
      <polygon points="72,181 64,195 48,195 40,181 48,167 64,167"/>
      <polygon points="72,235 64,249 48,249 40,235 48,221 64,221"/>
    </g>
    <line x1="56" y1="143" x2="56" y2="163" stroke="var(--gold)" stroke-width="1" stroke-dasharray="2 2"/>
    <line x1="56" y1="197" x2="56" y2="217" stroke="var(--gold)" stroke-width="1" stroke-dasharray="2 2"/>
    <g fill="var(--ink)">
      <circle cx="52" cy="124" r="2.5"/><circle cx="60" cy="128" r="2.5"/>
      <rect x="48" y="128" width="8" height="5" rx="2"/><rect x="56" y="132" width="8" height="4" rx="2"/>
      <circle cx="51" cy="178" r="2"/><circle cx="56" cy="178" r="2"/><circle cx="61" cy="178" r="2"/>
      <rect x="48" y="182" width="16" height="5" rx="2"/>
      <path d="M49 234h4v8h-4zM54 242v-8l3-5c1.5 0 2 1 1.7 2.4l-.7 2.6h4.5c1 0 1.5 1 1.2 1.8l-2 5.2c-.3.7-.9 1-1.6 1z"/>
    </g>
    <g stroke="var(--gold)" stroke-width="7" stroke-linejoin="round">
      <polygon role="img" aria-label="Photo: roofers at work on a house roof" points="430,259 395,320 325,320 290,259 325,198 395,198" fill="var(--photo-dark)"/>
      <polygon role="img" aria-label="Photo: metal roof sheets close up" points="328,292 312,320 280,320 264,292 280,264 312,264" fill="var(--photo-mid)"/>
    </g>
  </svg>

  <h2 class="abs process-title">VELL ROOFING <span class="accent">PROCESS</span></h2>
  <p class="abs step" style="top:112px">Complimentary consultation to access your roofing needs and review our honest recommendations</p>
  <p class="abs step" style="top:168px">Our team of professionals replace, restore, or repair your roof making the process as stress-free as possible.</p>
  <p class="abs step" style="top:222px">100% satisfaction, peace of mind, and continued professional coverage backed by VELL Protection</p>

  <div class="abs back-contact">
    <h2 class="contact-title">Contact <span>Us</span></h2>
    <p>Because we value your time as much as you value the roof over your head.</p>
  </div>

  <div class="abs divider back-divider"></div>

  <div class="abs phone-line back-phone">
    <svg width="14" height="14" viewBox="0 0 24 24"><circle cx="12" cy="12" r="12" fill="var(--gold)"/><path d="M8.2 6.5l2 2.2-1.1 1.6c.8 1.7 2 2.9 3.7 3.7l1.6-1.1 2.2 2-1.2 1.9c-4.6-.5-8.1-4-8.6-8.6z" fill="var(--ink)"/></svg>
    555.672.VELL
  </div>
  <div class="abs email-pill back-email">
    <svg width="9" height="7" viewBox="0 0 10 8"><rect x=".5" y=".5" width="9" height="7" fill="none" stroke="var(--gold)"/><path d="M.5 .5L5 4.5 9.5 .5" fill="none" stroke="var(--gold)"/></svg>
    info@vellroofing.example
  </div>
  <div class="abs web back-web">www.<b>vellroofing</b>.example</div>

  <div class="abs brand-name back-brand">Vell Roofing</div>
  <div class="abs stamp"></div>
  <div class="abs address-line" style="top:193px"></div>
  <div class="abs address-line" style="top:235px"></div>
  <div class="abs address-line" style="top:277px"></div>
  <div class="abs address-line" style="top:319px"></div>
</section>

</body>
</html>
```